Business Card

We need some ideas for corporate business cards. I'm interested in a double sided card, with one side featuring our corporate logo, the other side with employee information.

Corporate colors, logo etc. available at www.brivalo.com

Industry/Entity Type

Business

Requirements
Must have
• The "Brivalo" logo with stylized "O"

Nice to have
• Preferred font is calibri

```html
<!DOCTYPE html>
<html lang="en">
<head>
<meta charset="utf-8">
<title>Brivalo Business Card</title>
<link href="https://fonts.googleapis.com/css2?family=Carlito:wght@400;700&display=swap" rel="stylesheet">
<style>
  :root{
    --brand-blue:#536b99;
    --card-white:#ffffff;
    --ink:#2b2b2b;
    --ink-soft:#6b6b6b;
    --page:#e8e6e3;
  }
  *{box-sizing:border-box;margin:0;padding:0}
  html,body{width:1200px;height:997px;overflow:hidden}
  body{
    background:var(--page);
    font-family:"Carlito","Calibri",sans-serif;
    display:flex;flex-direction:column;align-items:center;justify-content:center;gap:60px;
  }
  .card{
    position:relative;width:700px;height:400px;
    box-shadow:0 4px 16px rgba(0,0,0,.12);
  }
  .card--brand{background:var(--brand-blue);color:var(--card-white)}
  .card--contact{background:var(--card-white);color:var(--ink)}

  .brand-name{
    position:absolute;font-weight:700;letter-spacing:.06em;text-transform:uppercase;
  }
  .card--brand .brand-name{left:100px;top:148px;font-size:104px;line-height:1;color:var(--card-white)}
  .card--contact .brand-name{left:46px;top:150px;font-size:58px;line-height:1;color:var(--brand-blue)}

  .web{
    position:absolute;font-size:15px;letter-spacing:.28em;
  }
  .card--brand .web{right:28px;bottom:26px;color:var(--card-white)}
  .card--contact .web{right:30px;top:26px;color:var(--brand-blue)}

  .person{position:absolute;right:110px;top:98px;text-align:right}
  .person__name{font-size:30px;color:var(--ink)}
  .person__role{font-size:19px;color:var(--ink-soft)}

  .contact-list{
    position:absolute;left:46px;bottom:36px;list-style:none;
    font-size:15px;line-height:1;color:var(--ink);
    display:flex;flex-direction:column;gap:9px;
  }
  .contact-list li{display:flex;align-items:center;gap:9px}
  .contact-list svg{width:14px;height:14px;fill:var(--ink-soft)}
</style>
</head>
<body>

<section class="card card--brand" aria-label="Card back">
  <div class="brand-name">Brivalo</div>
  <div class="web">www.brivalo.com</div>
</section>

<section class="card card--contact" aria-label="Card front">
  <div class="web">www.brivalo.com</div>
  <div class="person">
    <div class="person__name">Marcus Delane</div>
    <div class="person__role">Executive</div>
  </div>
  <div class="brand-name">Brivalo</div>
  <ul class="contact-list">
    <li><svg viewBox="0 0 16 16"><path d="M8 1 1 7.5h2V15h4v-4h2v4h4V7.5h2z"/></svg>2047 Larch Street, Halden, Alberta</li>
    <li><svg viewBox="0 0 16 16"><path d="M1 3h14v10H1z M1 3l7 6 7-6" stroke="#fff" stroke-width="1"/></svg>m.delane@brivalo.com</li>
    <li><svg viewBox="0 0 16 16"><path d="M1 5c0-2 3-3 7-3s7 1 7 3v1h-4V5H5v1H1zM3 8h10l1 6H2z"/></svg>001 0642 18 37 95</li>
    <li><svg viewBox="0 0 16 16"><path d="M4 0h1v2h5a1 1 0 0 1 1 1v12a1 1 0 0 1-1 1H5a1 1 0 0 1-1-1z M6 4v3h4V4z" /></svg>001 0642 18 37 95</li>
    <li><svg viewBox="0 0 16 16"><circle cx="8" cy="8" r="6.5" fill="none" stroke="#6b6b6b" stroke-width="1.3"/><path d="M1.5 8h13M8 1.5c-3 3-3 10 0 13M8 1.5c3 3 3 10 0 13" fill="none" stroke="#6b6b6b" stroke-width="1"/></svg>brivalo.com</li>
  </ul>
</section>

</body>
</html>
```